Real estate investment and development Business Visiting cards

Visiting cards for our company
We develop flats and rent them out, Now we planning to offer investors new investment opportunities in the UK Real estate sector. we used to have a design for our visiting card but we do not like it anymore. we want to have different designs keeping the same colors with our websites and company. I will attach our previous Visiting card model.

Target Market(s)

Private Investors, Banks,

Industry/Entity Type

Real Estate Development

Contact Information for Business Card

RVKT Holdings
Tomas Ferrell Director
Info to be included
3-Info

Tel
(+44 )7481 203917

Email

tomas@rvkt.co.uk

info@rvkt.co.uk

Address

17 Gorsefield Lane, Hollinwick, Marlbury, MB4 4RW

Website

rvktholdings.co.uk

Font styles to use
Serif

Colors
f78f20
fef5ee

Requirements
Must have
• The colours of the company and the Logo
Nice to have
• Modern idea and icons on the info
A code bar that directs to the website
Should not have
• a lot from the orange colour

```html
<!DOCTYPE html>
<html lang="en">
<head>
<meta charset="utf-8">
<title>RVKT Holdings – Business Cards</title>
<link rel="stylesheet" href="https://fonts.googleapis.com/css2?family=Tinos&family=Arimo:wght@400;700&display=swap">
<style>
  :root {
    --orange: #f78f20;
    --orange-dark: #c9680c;
    --orange-light: #f4a04a;
    --cream: #fef5ee;
    --ink: #111111;
    --grey: #6f6f6f;
    --rule: #9a9a9a;
    --paper: #ffffff;
    --backdrop: #e8e8e8;
  }
  * { box-sizing: border-box; margin: 0; padding: 0; }
  html, body {
    width: 1200px; height: 801px; overflow: hidden;
    background: var(--backdrop);
  }
  .sheet {
    position: relative; width: 1200px; height: 801px;
    display: flex; align-items: center; justify-content: center; gap: 60px;
  }
  .card {
    position: relative; width: 520px; height: 300px;
    box-shadow: 0 6px 18px rgba(0,0,0,0.18);
    overflow: hidden;
  }

  /* Front */
  .card-front { background: var(--paper); }
  .brand-square {
    position: absolute; left: 42px; top: 62px;
    width: 92px; height: 92px; background: var(--orange);
  }
  .wordmark {
    position: absolute; left: 156px; top: 50px;
    font-family: "Tinos", serif; font-size: 84px; line-height: 1;
    color: var(--ink); letter-spacing: 1px;
  }
  .identity {
    position: absolute; left: 42px; top: 180px; width: 212px;
    font-family: "Arimo", sans-serif;
  }
  .person-name {
    font-weight: 700; font-size: 20px; color: var(--orange);
    letter-spacing: 0.5px; text-transform: uppercase; white-space: nowrap;
  }
  .person-title {
    text-align: right; font-size: 14px; color: var(--grey); margin-top: 2px;
  }
  .address {
    font-size: 13.5px; color: var(--grey); line-height: 1.35; margin-top: 14px;
    white-space: nowrap;
  }
  .divider {
    position: absolute; left: 268px; top: 176px;
    width: 1px; height: 92px; background: var(--rule);
  }
  .contacts {
    position: absolute; left: 284px; top: 170px;
    list-style: none; font-family: "Arimo", sans-serif;
    font-size: 13.5px; color: var(--grey);
  }
  .contacts li {
    display: flex; align-items: center; gap: 8px; height: 24px; white-space: nowrap;
  }
  .contacts svg { width: 14px; height: 14px; flex: none; }

  /* Back */
  .card-back { background: var(--orange); }
  .back-texture {
    position: absolute; inset: 0;
    background: linear-gradient(135deg, var(--orange-dark) 0%, var(--orange) 45%, var(--orange-light) 100%);
  }
  .back-lockup {
    position: absolute; inset: 0;
    display: flex; align-items: center; justify-content: center; gap: 22px;
  }
  .back-square { width: 78px; height: 78px; background: var(--paper); }
  .back-wordmark {
    font-family: "Tinos", serif; font-size: 84px; line-height: 1;
    color: var(--ink); letter-spacing: 1px;
  }
</style>
</head>
<body>
<main class="sheet">

  <section class="card card-front" aria-label="Business card front">
    <div class="brand-square"></div>
    <div class="wordmark">RVKT</div>

    <div class="identity">
      <p class="person-name">Tomas Ferrell</p>
      <p class="person-title">Director</p>
      <p class="address">17 Gorsefield Lane<br>Hollinwick, Marlbury, MB4 4RW</p>
    </div>

    <div class="divider"></div>

    <ul class="contacts">
      <li>
        <svg viewBox="0 0 16 16" aria-hidden="true"><path fill="var(--orange)" d="M3.6 1.5l2.3 2.6-1.3 1.7c.9 2 2.6 3.7 4.6 4.6l1.7-1.3 2.6 2.3-1.4 2.1C6.5 13.4 2.6 9.5 1.5 3z"/></svg>
        <span>(+44 )7481 203917</span>
      </li>
      <li>
        <svg viewBox="0 0 16 16" aria-hidden="true"><rect x="1" y="3" width="14" height="10" fill="var(--orange)"/><path d="M1 3l7 6 7-6" fill="none" stroke="#fff" stroke-width="1.2"/></svg>
        <span>tomas@rvkt.co.uk</span>
      </li>
      <li>
        <svg viewBox="0 0 16 16" aria-hidden="true"><rect x="1" y="3" width="14" height="10" fill="var(--orange)"/><path d="M1 3l7 6 7-6" fill="none" stroke="#fff" stroke-width="1.2"/></svg>
        <span>info@rvkt.co.uk</span>
      </li>
      <li>
        <svg viewBox="0 0 16 16" aria-hidden="true"><circle cx="8" cy="8" r="7" fill="var(--orange)"/><path d="M1 8h14M8 1c3 3.5 3 10.5 0 14M8 1c-3 3.5-3 10.5 0 14" fill="none" stroke="#fff" stroke-width="1"/></svg>
        <span>www.rvktholdings.co.uk</span>
      </li>
    </ul>
  </section>

  <section class="card card-back" aria-label="Business card back">
    <div class="back-texture" role="img" aria-label="Embossed repeating brand pattern in orange tones"></div>
    <div class="back-lockup">
      <div class="back-square"></div>
      <div class="back-wordmark">RVKT</div>
    </div>
  </section>

</main>
</body>
</html>
```